Website Homepage Design

Talomere Care Partners Inc. is a Canadian financial services company that specialize in the delivery and administration of alternative health benefit solutions. Talomere is seeking to adjust their brand and develop a new website.

We like the design and layout of the website below but are not looking for an exact replica (be creative):

http://www.quellarvista.com/

We want the colour scheme to be clean white and "fresh green", possibly with orange accents (links).

This posting is only for a website homepage design (no coding), but anyone who includes a new logo, in addition to the design, will get priority.

Best of luck,

Oliver
Updates

Please let me know if you are currently working on a design.

Thank you,

Oliver

*Update:

Two example websites with good colour scheme/design:

- http://brindlepath.com/
- http://www.fettawaykidsnest.com.au/

I have attached a wireframe and colour scheme to the project brief. The main colour should be the green one. Other colours can be used for highlights and accents, etc.

Target Market(s)

Business owners age 50+

Industry/Entity Type

Financial

Requirements
Must have
• - Clear and simple design
- Area for video (similar to http://www.quellarvista.com)
Should not have
• - Lots of pictures

```html
<!DOCTYPE html>
<html lang="en">
<head>
<meta charset="utf-8">
<title>Talomere — Home</title>
<link rel="stylesheet" href="https://fonts.googleapis.com/css2?family=Anton&family=EB+Garamond:ital,wght@0,400;1,400&family=Open+Sans:wght@400;600;700&display=swap">
<style>
:root{
  --orange:#f57c00;
  --green:#4fae7f;
  --green-dark:#3a9268;
  --green-link:#1f7a3e;
  --apple:#8cc84b;
  --ink:#58584f;
  --text:#444;
  --muted:#777;
  --rule:#e3e6e4;
  --band:#f6f8f7;
}
*{margin:0;padding:0;box-sizing:border-box}
html,body{width:1200px;height:1019px;overflow:hidden;background:#fff}
body{position:relative;font-family:'Open Sans',sans-serif;color:var(--text)}
.abs{position:absolute}
.top-bar{left:0;top:0;width:1200px;height:3px;background:var(--orange)}
.login-btn{left:964px;top:14px;width:100px;height:35px;border-radius:4px;background:linear-gradient(#6cc497,var(--green-dark));border:1px solid #3b8a62;color:#fff;font-weight:700;font-size:13px;line-height:33px;text-align:center}
.brand{left:143px;top:49px;font-family:'EB Garamond',serif;font-size:34px;line-height:40px;color:var(--orange);display:flex;align-items:center;gap:5px}
.brand-dot{width:8px;height:8px;border-radius:50%;background:var(--green)}
.tagline{left:306px;top:68px;font-family:'EB Garamond',serif;font-size:14px;color:var(--muted)}
.tagline .easy{color:var(--orange)}
.tagline .afford{color:var(--green)}
.main-nav{right:136px;top:70px;font-family:'EB Garamond',serif;font-size:15px;color:var(--muted);display:flex}
.main-nav span{padding:0 7px;border-left:1px solid #ddd}
.main-nav span:first-child{border-left:0}
.main-nav span:last-child{padding-right:0}
.rule{height:1px;background:linear-gradient(90deg,transparent,var(--rule) 20%,var(--rule) 80%,transparent)}
.video-area{left:122px;top:143px;width:620px;height:345px;border-radius:14px 14px 40px 40px;background:linear-gradient(#e9e9ea,#c9c9cb 80%,#efefef)}
.video-screen{left:233px;top:170px;width:406px;height:261px;background:linear-gradient(135deg,#f7f7f7,#ffffff)}
.headline{left:716px;top:136px;font-family:'Anton',sans-serif;color:var(--ink);font-size:36px;line-height:50px;letter-spacing:1.4px}
.cost{left:716px;top:180px;font-family:'Anton',sans-serif;font-size:76px;line-height:96px;letter-spacing:1.5px;color:var(--ink)}
.cost .o{color:var(--orange)}
.apple{left:966px;top:182px;width:68px;height:78px;border-radius:14px;background:var(--apple)}
.lead{left:720px;top:272px;width:314px;font-size:13.4px;line-height:18px;color:var(--text);letter-spacing:.2px}
.cta{left:719px;top:354px;width:198px;height:52px;border-radius:4px;background:linear-gradient(#6dc79a,var(--green-dark));border:1px solid #3b8a62;color:#fff;font-size:21px;line-height:50px;text-align:center;letter-spacing:.3px}
.call{left:742px;top:417px;font-size:14px;color:#111}
.why-card{top:545px;width:282px;height:92px;background:linear-gradient(#fbfcfb,#f1f4f2);border-radius:4px;box-shadow:0 6px 8px -6px #d8dcd9}
.why-card .why{position:absolute;top:14px;font-family:'EB Garamond',serif;font-size:17px;color:var(--orange)}
.why-card .name{position:absolute;top:24px;font-family:'EB Garamond',serif;font-size:33px;color:var(--ink)}
.why-card .more{position:absolute;top:63px;font-size:14.5px;color:var(--ink);display:flex;align-items:center;gap:6px}
.quote-box{left:163px;top:719px;width:336px;height:150px;border:1px solid #cfd3d0;border-radius:30px 10px 30px 10px;background:#f8faf9}
.quote-tail{left:380px;top:866px}
.quote-mark{left:178px;top:728px;font-family:'EB Garamond',serif;font-size:64px;line-height:64px;color:#aaa}
.quote-text{left:184px;top:750px;width:310px;font-family:'EB Garamond',serif;font-style:italic;font-size:29px;line-height:30px;color:var(--ink);text-indent:38px}
.quote-who{left:383px;top:913px;font-size:12.5px;font-weight:600;color:var(--ink)}
.foot-col{top:737px}
.foot-col h3{font-weight:400;font-size:17.5px;color:var(--muted);margin-bottom:3px}
.foot-col p{font-size:12.3px;line-height:20px;color:var(--muted)}
.foot-col .live{color:var(--green-link)}
.seal{top:889px;height:34px;background:#e2e4e3;border-radius:4px}
.foot-band{left:0;top:958px;width:1200px;height:61px;background:var(--band)}
.copyright{left:131px;top:979px;font-size:11.5px;color:var(--muted)}
.follow{left:916px;top:979px;font-size:12.5px;color:var(--muted);display:flex;align-items:center;gap:5px}
.follow i{display:block;width:16px;height:16px;border-radius:2px;background:#9aa4ad}
</style>
</head>
<body>
<div class="abs top-bar"></div>

<header>
  <div class="abs login-btn">Login | Join</div>
  <div class="abs brand"><span>Talomere</span><span class="brand-dot"></span></div>
  <div class="abs tagline">We make it <span class="easy">easy.</span> We make it <span class="afford">affordable.</span></div>
  <nav class="abs main-nav">
    <span>Small Business</span><span>Big Business</span><span>Broker Business</span><span>Our Company</span><span>Contact Us</span>
  </nav>
  <div class="abs rule" style="left:260px;top:105px;width:710px"></div>
</header>

<section class="hero">
  <div class="abs video-area" role="img" aria-label="Laptop showing the site video preview"></div>
  <div class="abs video-screen" role="img" aria-label="Video area"></div>
  <div class="abs headline">Cut your healthcare</div>
  <div class="abs cost"><span class="o">CO$T</span> in</div>
  <div class="abs apple" role="img" aria-label="Green apple cut in half"></div>
  <p class="abs lead">We put control back in your hands by helping you reign in costs and maximize benefits. On average, you could save 20–30% over traditional group plans.</p>
  <div class="abs cta">Lest Get Started!</div>
  <div class="abs call">Call: 1-800-Tal-Care</div>
  <div class="abs rule" style="left:250px;top:501px;width:720px"></div>
</section>

<section class="why-list">
  <div class="abs why-card" style="left:152px">
    <span class="why" style="left:57px">why</span><span class="name" style="left:77px">smallbiz?</span>
    <span class="more" style="left:125px">Learn More <svg width="10" height="17" viewBox="0 0 10 17"><circle cx="5" cy="5" r="5" fill="#5daa2a"/><rect x="3" y="9" width="4" height="6" rx="1" fill="#5daa2a"/></svg></span>
  </div>
  <div class="abs why-card" style="left:462px">
    <span class="why" style="left:63px">why</span><span class="name" style="left:91px">bigbiz?</span>
    <span class="more" style="left:134px">Learn More <svg width="10" height="17" viewBox="0 0 10 17"><circle cx="5" cy="5" r="5" fill="#5daa2a"/><rect x="3" y="9" width="4" height="6" rx="1" fill="#5daa2a"/></svg></span>
  </div>
  <div class="abs why-card" style="left:768px">
    <span class="why" style="left:42px">why</span><span class="name" style="left:70px">brokerbiz?</span>
    <span class="more" style="left:142px">Learn More <svg width="10" height="17" viewBox="0 0 10 17"><circle cx="5" cy="5" r="5" fill="#5daa2a"/><rect x="3" y="9" width="4" height="6" rx="1" fill="#5daa2a"/></svg></span>
  </div>
  <div class="abs rule" style="left:380px;top:682px;width:500px"></div>
</section>

<footer>
  <div class="abs quote-box"></div>
  <svg class="abs quote-tail" width="60" height="48" viewBox="0 0 60 48"><path d="M8 2 L10 42 L52 2" fill="#f8faf9" stroke="#cfd3d0"/><rect x="9" y="0" width="44" height="3" fill="#f8faf9"/></svg>
  <div class="abs quote-mark">“</div>
  <p class="abs quote-text">Truely amazing. This is exactly what each financial services should be offering.</p>
  <div class="abs quote-who">– Guest Customer</div>

  <div class="abs foot-col" style="left:568px">
    <h3>Menu</h3>
    <p>Small Business<br>Big Business<br>Broker Business<br>Our Company<br>Contact Us</p>
  </div>
  <div class="abs foot-col" style="left:720px">
    <h3>Who We Are</h3>
    <p>About Us<br>Meet the Team<br>News<br>Careers</p>
  </div>
  <div class="abs foot-col" style="left:878px">
    <h3>Customer Service</h3>
    <p><span class="live">Click for Live Help!</span><br>Call us at 1-1800-Tal-Care<br>Email: info@talomere.com</p>
  </div>

  <div class="abs seal" style="left:761px;width:114px"></div>
  <div class="abs seal" style="left:881px;width:42px;border-radius:50%"></div>
  <div class="abs seal" style="left:937px;width:24px"></div>
  <div class="abs seal" style="left:970px;width:70px;border-radius:17px"></div>

  <div class="abs foot-band"></div>
  <div class="abs copyright">Copyright © 2010 Harlow Ridge Consulting Group Inc. Ver. 1.0.298</div>
  <div class="abs follow">Follow us&nbsp;<i></i><i></i><i></i></div>
</footer>
</body>
</html>
```